Business Card Design Project Bright Way

Simple and clean business card,

Logo and fond added in attachment

Data need to be changable:
Lien Varmeko
Customer Service Specialist

Bright Way - lien.varmeko@brightway-mail.be - Mob: +32471538046 - www.brightway-mail.be

Target Market(s)

Small businesses

Industry/Entity Type

Business

Requirements
Nice to have
• QR-code

```html
<!DOCTYPE html>
<html lang="en">
<head>
<meta charset="utf-8">
<title>Bright Way – Business Card</title>
<link href="https://fonts.googleapis.com/css2?family=Mulish:wght@400;700;800&display=swap" rel="stylesheet">
<style>
  :root {
    --page-bg: #eeeeec;
    --card-white: #ffffff;
    --brand-blue: #2fa3dc;
    --brand-green: #86c440;
    --green-light: #a0d468;
    --green-deep: #7cbb37;
    --text-on-green: #ffffff;
  }
  * { margin: 0; padding: 0; box-sizing: border-box; }
  html, body {
    width: 1200px;
    height: 1000px;
    overflow: hidden;
    background: var(--page-bg);
    font-family: "Mulish", sans-serif;
  }
  .canvas {
    position: relative;
    width: 1200px;
    height: 1000px;
  }
  .business-card {
    position: absolute;
    left: 150px;
    top: 230px;
    width: 900px;
    height: 540px;
    background: var(--card-white);
    overflow: hidden;
    box-shadow: 0 10px 30px rgba(0, 0, 0, 0.12);
  }
  .card-header {
    position: absolute;
    inset: 0 0 auto 0;
    height: 250px;
  }
  .brand {
    position: absolute;
    left: 66px;
    top: 178px;
    display: flex;
    align-items: center;
    gap: 14px;
  }
  .brand-mark {
    width: 34px;
    height: 34px;
    background: var(--brand-blue);
    border-radius: 4px;
  }
  .brand-name {
    font-weight: 700;
    font-size: 40px;
    color: var(--brand-green);
    line-height: 1;
  }
  .person {
    position: absolute;
    right: 64px;
    top: 66px;
    text-align: right;
    color: var(--brand-blue);
  }
  .person-name {
    font-weight: 800;
    font-size: 46px;
    line-height: 1.1;
  }
  .person-title {
    font-weight: 400;
    font-size: 30px;
    line-height: 1.2;
  }
  .card-footer {
    position: absolute;
    left: 0;
    right: 0;
    bottom: 0;
    height: 290px;
    background: var(--brand-green);
  }
  .footer-pattern {
    position: absolute;
    inset: 0;
    background: linear-gradient(180deg,
      var(--green-deep) 0%,
      var(--green-deep) 8%,
      var(--green-light) 8%,
      var(--green-light) 45%,
      var(--brand-green) 45%,
      var(--brand-green) 55%,
      var(--green-light) 55%,
      var(--green-light) 100%);
  }
  .contact-list {
    position: absolute;
    left: 70px;
    bottom: 58px;
    list-style: none;
    color: var(--text-on-green);
    font-size: 33px;
    line-height: 44px;
  }
  .contact-label { font-weight: 800; }
</style>
</head>
<body>
  <main class="canvas">
    <article class="business-card">
      <header class="card-header">
        <div class="brand">
          <span class="brand-mark" aria-hidden="true"></span>
          <span class="brand-name">Bright Way</span>
        </div>
        <div class="person">
          <h1 class="person-name">Lien Varmeko</h1>
          <p class="person-title">Customer Service Specialist</p>
        </div>
      </header>
      <section class="card-footer">
        <div class="footer-pattern" role="img" aria-label="Decorative green circuit pattern of lines and rings"></div>
        <ul class="contact-list">
          <li><span class="contact-label">Email</span>: lien.varmeko@brightway-mail.be</li>
          <li><span class="contact-label">Mobile</span>: +3 247 153 8046</li>
          <li><span class="contact-label">Website</span>: www.brightway-mail.be</li>
        </ul>
      </section>
    </article>
  </main>
</body>
</html>
```